Book Cover and Back Cover for Assemble Yourself™ Career Development Manual
Daniel R. Holbrook | Holbrook Advisory, LLC | danielrholbrook.example
Book Cover and Back Cover for Assemble Yourself™ Career Development Manual - Books
Creative Brief
BOOK COVER - blue (RGB 0.0.69) is background/foundational color - the title, "Assemble Yourself™", is orange (RGB 255.54.0), is centered - the subtitle, "A blueprint for utilizing the TRAV assessment to unlock your potential, develop your career, and advance your personal brand." is white, is centered - my name, "Daniel R. Holbrook", is at the bottom, is centered - graphic...I'd like to add a graphic at the bottom of the cover, please review my website, danielrholbrook.example, for ideas. I want it to marry the ideas of business strategy concepts, unlocking human potential, and career growth. BACK COVER - blue (RGB 0.0.69) is background/foundational color - at top center, in orange (RGB 255.54.0), "Inside this manual is the process that will unlock your potential", in a thinly outlined box - in the center is the text "Daniel R. Holbrook is a Licensed Conduct Pattern Examiner (LCPE), a Principal Expert in Staff Affairs (PESA) and a Kestrel Institute of World Commerce MBA graduate. He is owner of Holbrook Advisory, LLC, a coaching practice specializing in unlocking human potential and career advancement, is author of a book entitled Dreading Ordinariness, and is Assistant Director of the L. T. Brandt College of Commerce' Graduate Career Center where he provides career coaching to professional programs MBA students. Daniel is also Vice Chairman of the Phoenix Enterprise and Labor Growth council. Prior to his current roles, he spent more than a decade in recruitment, training and development, and operations management with organizations such as the Bright Harbor Inns and Retreats, VacaLink Worldwide, Meridel Care, and Silver Mesa College." - my picture, from http://danielrholbrook.example/about-2/, is incorporated into the above biography text - standard empty white box for ISBN barcode, at the bottom right - the "Holbrook Advisory" business logo, at bottom left
Books
Working professionals who are: - trying to discover their life's purpose - wanting a promotion at their current job - trying to transition to a different employer - looking for a step-by-step process
JPEG and PDF in 300dpi commercial printing use for 8x11 book cover with bleed

```html
<!DOCTYPE html>
<html lang="en">
<head>
<meta charset="utf-8">
<title>Assemble Yourself™ — Book Cover and Back Cover</title>
<link rel="stylesheet" href="https://fonts.googleapis.com/css2?family=Archivo+Black&family=Arimo:wght@400;700&family=Source+Sans+3:ital,wght@0,600;0,700;1,400&display=swap">
<style>
  :root {
    --navy: #000045;
    --navy-soft: #101565;
    --orange: #ff3600;
    --white: #ffffff;
    --page: #ffffff;
    --photo-top: #6a7f9a;
    --photo-bottom: #3a2e2a;
  }
  * { box-sizing: border-box; margin: 0; padding: 0; }
  html, body { width: 1200px; height: 849px; overflow: hidden; background: var(--page); }
  .spread { position: relative; width: 1200px; height: 849px; background: var(--page); }

  .cover { position: absolute; top: 19px; width: 552px; height: 804px; background: var(--navy); }
  .back-cover { left: 19px; }
  .front-cover { left: 629px; }

  /* Back cover */
  .teaser-box {
    position: absolute; left: 96px; top: 60px; width: 344px; height: 372px;
    border: 1px solid rgba(255,255,255,0.7);
    padding: 12px 14px;
  }
  .teaser-line {
    display: flex; justify-content: space-between;
    font-family: "Archivo Black", sans-serif;
    font-size: 38px; line-height: 49.5px;
    color: var(--orange);
    -webkit-text-stroke: 3px var(--white);
    paint-order: stroke fill;
    white-space: nowrap;
  }
  .bio {
    position: absolute; left: 77px; top: 456px; width: 410px;
    font-family: "Arimo", sans-serif; font-size: 11.4px; line-height: 15px;
    color: var(--white);
  }
  .author-photo {
    float: left; width: 82px; height: 106px; margin: 2px 14px 6px 0;
    background: linear-gradient(180deg, var(--photo-top), var(--photo-bottom));
  }
  .publisher-mark {
    position: absolute; left: 29px; top: 734px;
    display: flex; flex-direction: column; align-items: flex-start; gap: 5px;
    font-family: "Arimo", sans-serif; font-weight: 700; font-size: 10px; line-height: 11px;
    color: var(--white); letter-spacing: 0.5px;
  }
  .publisher-dot { width: 22px; height: 22px; border-radius: 50%; background: var(--white); }
  .isbn-box {
    position: absolute; left: 437px; top: 744px; width: 101px; height: 19px;
    background: var(--white);
    font-family: "Arimo", sans-serif; font-size: 7px; line-height: 19px;
    color: var(--navy); padding-left: 6px; white-space: nowrap;
  }

  /* Front cover */
  .title {
    position: absolute; left: 0; width: 100%; top: 190px; text-align: center;
    font-family: "Source Sans 3", sans-serif; font-weight: 600; font-size: 52px;
    color: var(--orange); letter-spacing: 0.3px;
  }
  .title sup { font-size: 14px; vertical-align: 28px; margin-left: 2px; }
  .subtitle {
    position: absolute; left: 50px; width: 460px; top: 263px; text-align: center;
    font-family: "Source Sans 3", sans-serif; font-style: italic; font-size: 15.5px; line-height: 20px;
    color: var(--white);
  }
  .cover-graphic {
    position: absolute; left: 194px; top: 336px; width: 210px; height: 312px;
    background: linear-gradient(180deg, var(--navy-soft), var(--navy));
  }
  .author-band {
    position: absolute; left: 122px; top: 720px; width: 298px; height: 53px;
    background: var(--white);
    display: flex; align-items: center; justify-content: center;
    font-family: "Source Sans 3", sans-serif; font-weight: 700; font-size: 22px;
    color: var(--navy); letter-spacing: 0.5px;
  }
</style>
</head>
<body>
<main class="spread">
  <section class="cover back-cover">
    <div class="teaser-box">
      <div class="teaser-line"><span>Inside</span><span>this</span></div>
      <div class="teaser-line"><span>manual</span><span>is</span></div>
      <div class="teaser-line"><span>the</span><span>process</span></div>
      <div class="teaser-line"><span>that</span><span>will</span></div>
      <div class="teaser-line"><span>u</span><span>n</span><span>l</span><span>o</span><span>c</span><span>k</span></div>
      <div class="teaser-line"><span>y</span><span>o</span><span>u</span><span>r</span></div>
      <div class="teaser-line"><span>p</span><span>o</span><span>t</span><span>e</span><span>n</span><span>t</span><span>i</span><span>a</span><span>l</span></div>
    </div>
    <div class="bio">
      <div class="author-photo" role="img" aria-label="Portrait photo of the author"></div>
      <p>Daniel R. Holbrook is a Licensed Conduct Pattern Examiner (LCPE), a Principal Expert in Staff Affairs (PESA) and a Kestrel Institute of World Commerce MBA graduate. He is owner of Holbrook Advisory, LLC, a coaching practice specializing in unlocking human potential and career advancement, is author of a book entitled Dreading Ordinariness, and is Assistant Director of the L. T. Brandt College of Commerce' Graduate Career Center where he provides career coaching to professional programs MBA students. Daniel is also Vice Chairman of the Phoenix Enterprise and Labor Growth council. Prior to his current roles, he spent more than a decade in recruitment, training and development, and operations management with organizations such as the Bright Harbor Inns and Retreats, VacaLink Worldwide, Meridel Care, and Silver Mesa College.</p>
    </div>
    <div class="publisher-mark">
      <span class="publisher-dot"></span>
      <span>HOLBROOK<br>ADVISORY</span>
    </div>
    <div class="isbn-box">ISBN 000-0-000000-00-0</div>
  </section>

  <section class="cover front-cover">
    <h1 class="title">Assemble Yourself<sup>™</sup></h1>
    <p class="subtitle">A blueprint for utilizing the TRAV assessment to unlock your potential, develop your career, and advance your personal brand</p>
    <div class="cover-graphic" role="img" aria-label="Line illustration of an open padlock in white outline"></div>
    <div class="author-band">DANIEL R. HOLBROOK</div>
  </section>
</main>
</body>
</html>
```